Dental Supplies Company - Email Marketing Campaign

I need a design suitable for email marketing (we use vision 6). We are a dental supply company and I would like to run a promotion on infection control including
- Cleaning Wipes
- Gloves
- Masks
- Sterilisation Monitoring Products

Roughly 6-8 product boxes.

Our website is talvexdentalsupplies.com.au

This will show you our general design layout and colours etc.

```html
<!DOCTYPE html>
<html lang="en">
<head>
<meta charset="utf-8">
<title>Talvex Dental Supplies – Infection Control Promotion</title>
<link href="https://fonts.googleapis.com/css2?family=Poppins:wght@500;600;700&family=Lato:wght@400;700;900&display=swap" rel="stylesheet">
<style>
:root{
  --teal:#137f9f;
  --teal-dark:#0f6f8c;
  --gold:#e8a923;
  --ink:#111111;
  --grey-text:#555a5e;
  --panel:#f0f0f2;
  --card-bg:#ffffff;
  --white:#ffffff;
}
*{margin:0;padding:0;box-sizing:border-box}
html,body{width:1200px;height:3172px;overflow:hidden;background:var(--white)}
body{position:relative;font-family:'Lato',sans-serif;color:var(--ink)}
.abs{position:absolute}

/* header */
.brand{left:67px;top:62px;display:flex;align-items:center;gap:16px}
.brand-dot{width:70px;height:70px;border-radius:50%;background:var(--teal)}
.brand-name{font-family:'Lato',sans-serif;font-weight:700;font-size:40px;color:var(--teal);line-height:1}
.contact-top{left:813px;top:82px;font-size:27px;line-height:33px;color:var(--ink)}

.nav{left:0;top:185px;width:1200px;height:90px;background:var(--teal);display:flex;justify-content:center;align-items:center}
.nav a{color:var(--white);text-decoration:none;font-size:23px;letter-spacing:.3px;padding:0 21px;line-height:36px;border-left:1px solid rgba(255,255,255,.35)}
.nav a:first-child{border-left:none}

/* hero */
.hero-photo{left:540px;top:275px;width:660px;height:645px;background:linear-gradient(90deg,#ffffff 0%,#eef2f1 22%,#d9c3b2 48%,#9fd3c8 70%,#7fc7ba 100%)}
.tag{left:74px;top:421px;height:65px;width:508px;background:var(--gold);clip-path:polygon(0 0,100% 0,96% 50%,100% 100%,0 100%,4% 50%);color:var(--white);font-weight:700;font-size:25px;display:flex;align-items:center;padding-left:31px;letter-spacing:.2px}
.hero-title{left:72px;top:503px;width:600px;font-family:'Poppins',sans-serif;font-weight:700;font-size:56px;line-height:58px;color:var(--ink);letter-spacing:-.5px}
.hero-copy{left:72px;top:694px;width:600px;font-size:25.5px;line-height:32px;color:var(--grey-text)}

.section-title{left:67px;top:1016px;font-family:'Poppins',sans-serif;font-weight:500;font-size:50px;color:var(--gold)}

/* cards */
.card{width:339px;background:var(--card-bg);box-shadow:0 10px 10px -6px rgba(0,0,0,.25);text-align:center}
.card-photo{height:326px;background:var(--panel);display:flex;align-items:center;justify-content:center}
.card-photo span{display:block;width:240px;height:200px;border-radius:12px}
.card-body{height:312px;padding-top:51px}
.badge{display:inline-block;background:var(--gold);color:var(--white);font-size:20px;line-height:32px;padding:0 15px;border-radius:16px}
.card-title{font-family:'Poppins',sans-serif;font-weight:600;font-size:24px;line-height:30px;margin-top:8px}
.card-sub{font-size:20px;line-height:26px;color:#3a3d40}
.card-price{font-size:25px;font-weight:700;color:var(--teal);line-height:34px}
.btn{display:inline-block;margin-top:26px;background:var(--teal);color:var(--white);font-weight:700;font-size:23px;line-height:44px;width:162px}

.perk{left:67px;top:2584px;width:775px;height:113px;background:var(--panel);border-left:22px solid var(--teal);padding:26px 0 0 33px;font-size:27px;line-height:32px}
.perk b{font-weight:700}
.cta{left:156px;top:2782px;width:848px;height:85px;background:var(--gold);border-radius:9px;color:var(--white);font-weight:900;font-size:32px;display:flex;align-items:center;justify-content:center;letter-spacing:.2px}

.footer{left:0;top:2950px;width:1200px;height:222px;background:var(--teal);color:var(--white)}
.foot-line{left:116px;font-size:30px;line-height:36px}
.foot-ico{left:68px;width:24px;height:24px}
.social{top:42px;width:56px;height:56px;border-radius:50%;background:var(--white)}
.site{right:65px;top:106px;font-size:30px}
</style>
</head>
<body>

<header>
  <div class="abs brand"><span class="brand-dot"></span><span class="brand-name">Talvex Dental Supplies</span></div>
  <div class="abs contact-top">1300 555 019<br>talvexdentalsupplies.com.au</div>
</header>

<nav class="abs nav">
  <a href="#">SHOP</a><a href="#">ABOUT US</a><a href="#">INFECTION CONTROL</a><a href="#">INSTRUMENTS</a>
</nav>

<section class="hero">
  <div class="abs hero-photo" role="img" aria-label="Clinician wearing a surgical face mask and teal gloves"></div>
  <div class="abs tag">INFECTION CONTROL PROMOTION</div>
  <h1 class="abs hero-title">Everything You Need to Stay Compliant &amp; Protected</h1>
  <p class="abs hero-copy">From gloves and masks to sterilisation monitoring stock up on essentials and save up to 15% across our infection control range.</p>
</section>

<h2 class="abs section-title">Featured Products</h2>

<article class="abs card" style="left:67px;top:1124px">
  <div class="card-photo"><span role="img" aria-label="Box of nitrile examination gloves with a blue glove" style="background:linear-gradient(135deg,#dfe6f2,#7fb0e6)"></span></div>
  <div class="card-body"><span class="badge">SAVE 15%</span><div class="card-title">Examination Gloves</div><div class="card-sub">Nitrile, Latex &amp; Vinyl</div><div class="card-price">From $12.95 / box</div><span class="btn">SHOP NOW</span></div>
</article>
<article class="abs card" style="left:433px;top:1124px">
  <div class="card-photo"><span role="img" aria-label="Surgical face mask on a display head beside its box" style="background:linear-gradient(135deg,#d8dde2,#bcd6e6)"></span></div>
  <div class="card-body"><span class="badge">SAVE 10%</span><div class="card-title">Face Masks</div><div class="card-sub">Surgical &amp; P2/N95</div><div class="card-price">From $8.50 / box</div><span class="btn">SHOP NOW</span></div>
</article>
<article class="abs card" style="left:798px;top:1124px">
  <div class="card-photo"><span role="img" aria-label="Tubs and packs of surface disinfectant wipes" style="background:linear-gradient(135deg,#e6f1ee,#6fbfa8)"></span></div>
  <div class="card-body"><span class="badge">SAVE 12%</span><div class="card-title">Cleaning Wipes</div><div class="card-sub">Surface Disinfectant</div><div class="card-price">From $18.00 / tub</div><span class="btn">SHOP NOW</span></div>
</article>

<article class="abs card" style="left:67px;top:1847px">
  <div class="card-photo"><span role="img" aria-label="Handheld sterilisation labelling gun" style="background:linear-gradient(135deg,#d9dcde,#3b4247)"></span></div>
  <div class="card-body"><span class="badge">SAVE 10%</span><div class="card-title">Sterilisation Monitoring</div><div class="card-sub">Nitrile, Latex &amp; Vinyl</div><div class="card-price">From $32.00 / pack</div><span class="btn">SHOP NOW</span></div>
</article>
<article class="abs card" style="left:433px;top:1847px">
  <div class="card-photo"><span role="img" aria-label="Stacked boxes of sterilisation pouches" style="background:linear-gradient(135deg,#e2e8ec,#1d5f88)"></span></div>
  <div class="card-body"><span class="badge">SAVE 8%</span><div class="card-title">Sterilisation Pouches</div><div class="card-sub">Surgical &amp; P2/N95</div><div class="card-price">From $14.50 / box</div><span class="btn">SHOP NOW</span></div>
</article>
<article class="abs card" style="left:798px;top:1847px">
  <div class="card-photo"><span role="img" aria-label="Pump bottle of antibacterial hand sanitiser" style="background:linear-gradient(135deg,#eef0f3,#b04d8f)"></span></div>
  <div class="card-body"><span class="badge">SAVE 10%</span><div class="card-title">Hand Sanitiser</div><div class="card-sub">Surface Disinfectant</div><div class="card-price">From $9.95 / unit</div><span class="btn">SHOP NOW</span></div>
</article>

<div class="abs perk"><b>Free delivery on orders over $150</b><br>Same-day dispatch available · 100% money-back guarantee</div>

<div class="abs cta">VIEW ALL INFECTION CONTROL PRODUCTS</div>

<footer class="abs footer">
  <svg class="abs foot-ico" style="top:49px" viewBox="0 0 24 24" fill="none" stroke="#fff" stroke-width="1.8"><circle cx="12" cy="12" r="10.5"/><path d="M12 18s-4-4.2-4-7a4 4 0 0 1 8 0c0 2.8-4 7-4 7z"/><circle cx="12" cy="10.8" r="1.3"/></svg>
  <div class="abs foot-line" style="top:43px">12 Kestrel Way, Ravenhall, VIC 3023</div>
  <svg class="abs foot-ico" style="top:88px" viewBox="0 0 24 24" fill="none" stroke="#fff" stroke-width="1.8"><circle cx="12" cy="12" r="10.5"/><path d="M8.5 7.5l2 .2.8 2.2-1.2 1a6 6 0 0 0 3 3l1-1.2 2.2.8.2 2c-.5.8-1.5 1.2-2.5 1A9 9 0 0 1 7.5 10c-.2-1 .2-2 1-2.5z"/></svg>
  <div class="abs foot-line" style="top:82px">1300 555 019</div>
  <svg class="abs foot-ico" style="top:127px" viewBox="0 0 24 24" fill="none" stroke="#fff" stroke-width="1.8"><circle cx="12" cy="12" r="10.5"/><rect x="7" y="8.5" width="10" height="7" rx="1"/><path d="M7 9l5 4 5-4"/></svg>
  <div class="abs foot-line" style="top:121px">sales@talvex.com.au</div>
  <div class="abs social" style="left:945px"></div>
  <div class="abs social" style="left:1012px"></div>
  <div class="abs social" style="left:1079px"></div>
  <div class="abs site">talvexdentalsupplies.com.au</div>
</footer>

</body>
</html>
```